Vacation giveaway landing page design

We are giving away a holiday/vacation to Rome and we need a landing page designed that will entice people to enter their email address for a chance to win!

Full brief, examples and everything else can be found in this document: https://files.quorvanshare.net/page/7-tmzrwpQY4vxkaLn8sbgeXu2fcTo5kWdn3jhpyuBc29m/open?mode=viewing

Number of Pages Required

1 page

```html
<!DOCTYPE html>
<html lang="en">
<head>
<meta charset="utf-8">
<title>Wanderlot – Win a Holiday in Rome</title>
<link href="https://fonts.googleapis.com/css2?family=Raleway:wght@600;700;800&family=Barlow:wght@400;500;600&family=Dancing+Script:wght@600&display=swap" rel="stylesheet">
<style>
:root{
  --hero-bg:#f0efee;
  --ink:#3b3b3b;
  --muted:#8d8d8d;
  --brown:#9c7049;
  --brown-dark:#6e4a2e;
  --gold:#c79a55;
  --yellow:#f2c12e;
  --red:#e84a48;
  --line:#e6e6e6;
  --white:#ffffff;
}
*{box-sizing:border-box;margin:0;padding:0}
html,body{width:860px;height:1200px;overflow:hidden;background:var(--white)}
body{font-family:'Barlow',sans-serif;color:var(--ink);position:relative}
.page{position:relative;width:860px;height:1200px;overflow:hidden}
.hero-bg{position:absolute;left:0;top:0;width:860px;height:505px;background:var(--hero-bg)}
.photo{position:absolute;left:0;top:0;width:860px;height:640px}
.brand{position:absolute;left:0;width:860px;display:flex;justify-content:center;align-items:center;gap:8px}
.brand-mark{width:26px;height:26px;border-radius:50%;border:2px solid var(--brown)}
.brand-name{font-family:'Raleway',sans-serif;font-weight:800;font-size:22px;color:var(--brown);letter-spacing:1px;text-transform:uppercase}
.brand--top{top:28px}
.brand--bottom{top:1147px}
.center{position:absolute;left:0;width:860px;text-align:center}
.tagline{top:118px;font-family:'Dancing Script',cursive;font-size:15px;color:var(--gold)}
.headline{top:141px;font-family:'Raleway',sans-serif;font-weight:700;font-size:18px;color:var(--ink)}
.city{top:164px;font-family:'Raleway',sans-serif;font-weight:800;font-size:31px;color:var(--brown)}
.intro{top:214px;font-size:9.8px;line-height:15px;color:#444}
.intro b{font-weight:600}
.perks{position:absolute;top:256px;left:0;width:860px;font-size:12.5px;color:#444}
.perk{position:absolute;display:flex;align-items:center;gap:6px}
.perk svg{width:11px;height:9px}
.label{top:301px;font-size:8.2px;font-weight:500;letter-spacing:.6px;display:flex;justify-content:center;align-items:center;gap:5px}
.field{position:absolute;background:var(--white);border:1px solid #ececec;display:flex;align-items:center;font-size:7.6px;color:#c4c4c4}
.field--hero{left:349px;top:319px;width:162px;height:27px;justify-content:center;letter-spacing:.4px}
.btn{position:absolute;background:var(--yellow);color:var(--white);display:flex;align-items:center;justify-content:center;font-weight:500;letter-spacing:.3px}
.btn--hero{left:349px;top:362px;width:162px;height:32px;font-size:9.5px}
.legal{top:413px;font-size:7.5px;line-height:15px;color:var(--muted)}
.legal b{color:#666;font-weight:500}
.winners-title{top:561px;font-family:'Raleway',sans-serif;font-weight:700;font-size:19.5px;color:var(--ink)}
.winners-sub{top:587px;font-size:10.6px;font-weight:500;letter-spacing:.3px;color:#444}
.card{position:absolute;width:328px;height:118px;border:1px solid var(--line);background:var(--white)}
.avatar{position:absolute;left:12px;top:15px;width:86px;height:86px;border-radius:50%}
.name{position:absolute;left:108px;top:23px;display:flex;align-items:baseline;gap:9px;white-space:nowrap}
.name h3{font-family:'Raleway',sans-serif;font-weight:700;font-size:11.4px;color:#4a4a4a;letter-spacing:.2px}
.name span{font-size:8.8px;color:var(--gold)}
.desc{position:absolute;left:108px;top:45px;width:205px;font-size:8.4px;line-height:14px;color:#333}
.desc em{font-style:normal;color:var(--muted);display:block}
.stats{position:absolute;left:108px;top:95px;display:flex;gap:12px;font-size:8px;color:#b5b5b5}
.stat{display:flex;align-items:center;gap:4px}
.stat svg{width:9px;height:8px}
.stat--liked{color:var(--red)}
.ribbon{position:absolute;left:230px;top:100px;width:116px;height:28px}
.ribbon-text{position:absolute;left:0;top:4px;width:108px;text-align:center;font-size:8.6px;line-height:9.6px;font-weight:600;color:var(--white)}
.ribbon-text span{color:#ffd86a;display:block}
.nav-arrow{position:absolute;top:776px;width:12px;height:20px}
.dots{position:absolute;top:963px;left:417px;display:flex;gap:6px}
.dot{width:4px;height:4px;border-radius:50%;background:#ddd}
.dot--active{width:5px;height:5px;background:var(--brown)}
.cta{position:absolute;left:0;top:1000px;width:860px;height:119px;background:linear-gradient(90deg,#6a4329,#8b5e3b 50%,#6f4a30)}
.cta-title{position:absolute;left:154px;top:29px;font-family:'Raleway',sans-serif;font-weight:800;font-size:19.5px;color:var(--white)}
.cta-text{position:absolute;left:155px;top:63px;font-size:9.7px;line-height:15px;color:var(--white)}
.cta-label{position:absolute;left:470px;top:33px;font-size:8px;font-weight:600;color:var(--white);letter-spacing:.3px}
.field--cta{left:471px;top:49px;width:129px;height:27px;padding-left:10px;font-size:8.4px;color:#b9b9b9}
.btn--cta{left:615px;top:49px;width:129px;height:27px;font-size:8.4px}
</style>
</head>
<body>
<main class="page">
  <div class="hero-bg"></div>

  <svg class="photo" viewBox="0 0 860 640" role="img" aria-label="Photo of the Colosseum arches in warm evening light">
    <defs><linearGradient id="tl" x1="0" y1="0" x2="1" y2="1"><stop offset="0" stop-color="#b0805e"/><stop offset="1" stop-color="#8a6248"/></linearGradient></defs>
    <path d="M32 0H322C300 40 268 80 230 92C190 100 120 88 60 40Z" fill="url(#tl)"/>
  </svg>
  <svg class="photo" viewBox="0 0 860 640" role="img" aria-label="Photo of the Colosseum facade against a pale sky">
    <defs><linearGradient id="tr" x1="0" y1="0" x2="0" y2="1"><stop offset="0" stop-color="#b89f86"/><stop offset="1" stop-color="#6e5440"/></linearGradient></defs>
    <path d="M620 0H860V250C830 280 790 295 760 285L640 225C615 212 608 190 612 160L622 30Z" fill="url(#tr)"/>
  </svg>
  <svg class="photo" viewBox="0 0 860 640" role="img" aria-label="Photo of Saint Peter's Basilica dome in soft pink light">
    <defs><linearGradient id="bl" x1="0" y1="0" x2="0" y2="1"><stop offset="0" stop-color="#ecd6cb"/><stop offset=".5" stop-color="#c9a486"/><stop offset="1" stop-color="#d9c2ad"/></linearGradient></defs>
    <path d="M0 230C40 205 110 195 150 215L270 330C295 355 300 400 285 440L200 580C180 610 140 620 100 600L0 560Z" fill="url(#bl)"/>
  </svg>
  <svg class="photo" viewBox="0 0 860 640" role="img" aria-label="Photo of a traveller in a black hat looking at the Colosseum">
    <defs><linearGradient id="br" x1="0" y1="0" x2="0" y2="1"><stop offset="0" stop-color="#8fb9de"/><stop offset=".45" stop-color="#a8957e"/><stop offset="1" stop-color="#3c302a"/></linearGradient></defs>
    <path d="M700 375C720 365 760 360 790 368C820 385 850 420 860 440V550L800 615C775 635 740 630 715 615L640 560C620 545 615 520 620 495L630 420C635 395 660 385 700 375Z" fill="url(#br)"/>
  </svg>

  <div class="brand brand--top"><span class="brand-mark"></span><span class="brand-name">Wanderlot</span></div>

  <p class="center tagline">Always had dreams to visit Rome?</p>
  <h1 class="center headline">Your next Holiday could be in</h1>
  <h2 class="center city">The Eternal City</h2>
  <p class="center intro">Enter your email to have a chance to win a<br><b>FREE</b> holiday in Rome that include:</p>

  <ul class="perks">
    <li class="perk" style="left:271px"><svg viewBox="0 0 11 9"><path d="M1 4.5L4 7.5L10 1" fill="none" stroke="#f2c12e" stroke-width="1.6"/></svg>4 Nights for 2 People</li>
    <li class="perk" style="left:420px"><svg viewBox="0 0 11 9"><path d="M1 4.5L4 7.5L10 1" fill="none" stroke="#f2c12e" stroke-width="1.6"/></svg>Flights</li>
    <li class="perk" style="left:510px"><svg viewBox="0 0 11 9"><path d="M1 4.5L4 7.5L10 1" fill="none" stroke="#f2c12e" stroke-width="1.6"/></svg>Hotel ★ ★ ★ ★</li>
  </ul>

  <p class="center label"><svg width="10" height="8" viewBox="0 0 10 8"><rect x=".5" y=".5" width="9" height="7" fill="none" stroke="#444"/><path d="M.5 .5L5 4.5L9.5 .5" fill="none" stroke="#444"/></svg>EMAIL ADDRESS</p>
  <div class="field field--hero">YOUR FANCY EMAIL</div>
  <div class="btn btn--hero">ENTER NOW</div>
  <p class="center legal">By entering your email address, you agree to receive updates<br>about the competition and Wanderlot. You can<br>review our competition terms and conditions <b>Here</b></p>

  <h2 class="center winners-title">Still Not Sure?</h2>
  <p class="center winners-sub">SEE OUR PREVIOUS WINNERS</p>

  <svg class="nav-arrow" style="left:29px" viewBox="0 0 12 20"><path d="M10 2L2 10L10 18" fill="none" stroke="#999" stroke-width="1.2"/></svg>
  <svg class="nav-arrow" style="left:801px" viewBox="0 0 12 20"><path d="M2 2L10 10L2 18" fill="none" stroke="#999" stroke-width="1.2"/></svg>

  <article class="card" style="left:82px;top:649px">
    <div class="avatar" role="img" aria-label="Photo of the November winner with a friend" style="background:linear-gradient(135deg,#c9b59c,#6b5a4c)"></div>
    <div class="name"><h3>NINA CASTELL</h3><span>November’s Winner</span></div>
    <p class="desc">Congrats to this month's winner - Nina Castell<em>Read more</em></p>
    <div class="stats">
      <span class="stat stat--liked"><svg viewBox="0 0 10 9"><path d="M5 9L1 5A2.3 2.3 0 0 1 5 1.5A2.3 2.3 0 0 1 9 5Z" fill="#e84a48"/></svg>25</span>
      <span class="stat"><svg viewBox="0 0 10 9"><ellipse cx="5" cy="4" rx="4.5" ry="3.6" fill="#bbb"/></svg>12</span>
      <span class="stat"><svg viewBox="0 0 10 9"><path d="M1 8C2 4 5 3 7 3V1L10 4L7 7V5C4 5 2 6 1 8Z" fill="#bbb"/></svg>8</span>
    </div>
    <svg class="ribbon" viewBox="0 0 116 28"><path d="M0 0H116L108 7L114 14L106 21L112 28H0Z" fill="#e84a48"/></svg>
    <p class="ribbon-text" style="left:230px;top:104px">A GETAWAY IN ROME<span>ITALY</span></p>
  </article>

  <article class="card" style="left:433px;top:649px">
    <div class="avatar" role="img" aria-label="Photo of the December winner" style="background:linear-gradient(135deg,#3d6e8c,#8c3f6b)"></div>
    <div class="name"><h3>ELSA BRANDT</h3><span>December’s Winner</span></div>
    <p class="desc">Looks like Elsa is the lucky one this month as she's won a trip to Valencia! What a Christmas present!<em>Read more</em></p>
    <div class="stats">
      <span class="stat"><svg viewBox="0 0 10 9"><path d="M5 9L1 5A2.3 2.3 0 0 1 5 1.5A2.3 2.3 0 0 1 9 5Z" fill="#ccc"/></svg>18</span>
      <span class="stat"><svg viewBox="0 0 10 9"><ellipse cx="5" cy="4" rx="4.5" ry="3.6" fill="#bbb"/></svg>24</span>
      <span class="stat"><svg viewBox="0 0 10 9"><path d="M1 8C2 4 5 3 7 3V1L10 4L7 7V5C4 5 2 6 1 8Z" fill="#bbb"/></svg>12</span>
    </div>
    <svg class="ribbon" viewBox="0 0 116 28"><path d="M0 0H116L108 7L114 14L106 21L112 28H0Z" fill="#e84a48"/></svg>
    <p class="ribbon-text" style="left:230px;top:104px">HOLIDAY IN VALENCIA<span>SPAIN</span></p>
  </article>

  <article class="card" style="left:82px;top:793px">
    <div class="avatar" role="img" aria-label="Photo of the January winner in a city street" style="background:linear-gradient(135deg,#8a7a62,#2e2623)"></div>
    <div class="name"><h3>PRIYA SOLANKI</h3><span>January’s Winner</span></div>
    <p class="desc">Priya Solanki is the lucky winner this month!<em>Read more</em></p>
    <div class="stats">
      <span class="stat"><svg viewBox="0 0 10 9"><path d="M5 9L1 5A2.3 2.3 0 0 1 5 1.5A2.3 2.3 0 0 1 9 5Z" fill="#ccc"/></svg>62</span>
      <span class="stat"><svg viewBox="0 0 10 9"><ellipse cx="5" cy="4" rx="4.5" ry="3.6" fill="#bbb"/></svg>12</span>
      <span class="stat"><svg viewBox="0 0 10 9"><path d="M1 8C2 4 5 3 7 3V1L10 4L7 7V5C4 5 2 6 1 8Z" fill="#bbb"/></svg>18</span>
    </div>
    <svg class="ribbon" viewBox="0 0 116 28"><path d="M0 0H116L108 7L114 14L106 21L112 28H0Z" fill="#e84a48"/></svg>
    <p class="ribbon-text" style="left:230px;top:104px;color:#fff">A NORTHERN LIGHTS<br>GETAWAY</p>
  </article>

  <article class="card" style="left:433px;top:793px">
    <div class="avatar" role="img" aria-label="Photo of the February winner outdoors" style="background:linear-gradient(135deg,#a99678,#dfe3ea)"></div>
    <div class="name"><h3>MARTIN HALE</h3><span>February’s Winner</span></div>
    <p class="desc">New York, New York! Congratulations to Martin Hale - he's won flights for two to the Big Apple.<em>Read more</em></p>
    <div class="stats">
      <span class="stat"><svg viewBox="0 0 10 9"><path d="M5 9L1 5A2.3 2.3 0 0 1 5 1.5A2.3 2.3 0 0 1 9 5Z" fill="#ccc"/></svg>47</span>
      <span class="stat"><svg viewBox="0 0 10 9"><ellipse cx="5" cy="4" rx="4.5" ry="3.6" fill="#bbb"/></svg>9</span>
      <span class="stat"><svg viewBox="0 0 10 9"><path d="M1 8C2 4 5 3 7 3V1L10 4L7 7V5C4 5 2 6 1 8Z" fill="#bbb"/></svg>2</span>
    </div>
    <svg class="ribbon" viewBox="0 0 116 28"><path d="M0 0H116L108 7L114 14L106 21L112 28H0Z" fill="#e84a48"/></svg>
    <p class="ribbon-text" style="left:230px;top:104px">FLIGHTS TO<span>NEW YORK CITY</span></p>
  </article>

  <div class="dots"><span class="dot dot--active"></span><span class="dot"></span><span class="dot"></span></div>

  <section class="cta" role="img" aria-label="Band with a dimmed photo of the Colosseum interior">
    <h2 class="cta-title">Save your spot now!</h2>
    <p class="cta-text">Enter your email address to have a chance<br>to win a Holiday in Rome</p>
    <p class="cta-label">EMAIL ADDRESS</p>
    <div class="field field--cta">Email Address</div>
    <div class="btn btn--cta">ENTER NOW!</div>
  </section>

  <div class="brand brand--bottom"><span class="brand-mark"></span><span class="brand-name">Wanderlot</span></div>
</main>
</body>
</html>
```